Letterhead for Dorian Welk

I need a letterhead based on the business card design

Industry/Entity Type

Business

Requirements
Must have
• Footer: Dorian Welk Naturopath
Shop 4123c, 46 Carrow Lane, Sydney 2000

```html
<!DOCTYPE html>
<html lang="en">
<head>
<meta charset="utf-8">
<title>Dorian Welk Naturopath – Letterhead</title>
<link rel="stylesheet" href="https://fonts.googleapis.com/css2?family=Montserrat:wght@600&family=Open+Sans:wght@400&display=swap">
<style>
  :root {
    --orange: #f7901e;
    --orange-deep: #e9801a;
    --peach-soft: rgba(247, 144, 30, 0.13);
    --white: #ffffff;
    --ink: #1a1a1a;
  }
  html, body {
    margin: 0;
    padding: 0;
    overflow: hidden;
    background: var(--white);
  }
  .letterhead {
    position: relative;
    width: 900px;
    height: 1200px;
    overflow: hidden;
    background: var(--white);
  }
  .header-band {
    position: absolute;
    top: 0;
    left: 0;
    width: 900px;
    height: 118px;
    background: var(--orange);
  }
  .header-texture {
    position: absolute;
    top: 0;
    right: 0;
    width: 500px;
    height: 118px;
    background: linear-gradient(90deg, rgba(233, 128, 26, 0) 0%, rgba(214, 112, 18, 0.35) 100%);
  }
  .header-rule {
    position: absolute;
    top: 124px;
    left: 0;
    width: 900px;
    height: 5px;
    background: var(--orange);
  }
  .brand-name {
    position: absolute;
    top: 42px;
    left: 40px;
    width: 160px;
    margin: 0;
    text-align: center;
    font-family: "Montserrat", sans-serif;
    font-weight: 600;
    font-size: 23px;
    line-height: 28px;
    letter-spacing: 0.5px;
    color: var(--white);
    white-space: nowrap;
  }
  .leaf-backdrop {
    position: absolute;
    top: 130px;
    left: 0;
    width: 340px;
    height: 1070px;
    background: linear-gradient(90deg, var(--peach-soft) 0%, rgba(247, 144, 30, 0.08) 60%, rgba(247, 144, 30, 0) 100%);
    border-top-right-radius: 100% 60%;
    border-bottom-right-radius: 40% 30%;
  }
  .footer-tab {
    position: absolute;
    top: 1101px;
    left: 0;
    width: 403px;
    height: 48px;
  }
  .footer-details {
    position: absolute;
    top: 1104px;
    left: 14px;
    margin: 0;
    font-family: "Open Sans", sans-serif;
    font-weight: 400;
    font-size: 15px;
    line-height: 21px;
    color: var(--ink);
    font-style: normal;
  }
</style>
</head>
<body>
  <div class="letterhead">
    <div class="leaf-backdrop" role="img" aria-label="Large faint leaf with veins, decorative background"></div>

    <header>
      <div class="header-band"></div>
      <div class="header-texture" role="img" aria-label="Geometric faceted triangle pattern in orange tones"></div>
      <div class="header-rule"></div>
      <p class="brand-name">DORIAN WELK</p>
    </header>

    <footer>
      <svg class="footer-tab" viewBox="0 0 403 48" aria-hidden="true">
        <polygon points="0,0 356,0 403,48 0,48" fill="var(--orange)"/>
      </svg>
      <address class="footer-details">
        Dorian Welk Naturopath<br>
        Shop 4123c, 46 Carrow Lane, Sydney 2000
      </address>
    </footer>
  </div>
</body>
</html>
```